Wine Label for a syrah wine hand crafted from walla walla valley, washington

design a wine label for the name of the brand: Orvanel. It is a wine hand crafted from Walla Walla Valley in Washington state. the label should be landscape in design, 95 mm wide by 85 mm tall. it should include the name of the brand, Orvanel, Walla Walla Valley, 2020 and Syrah. the brand is called orvanel with this in mind:

-orvanel Definition & Meaning |
1. : having (something) at the center. The solar system is helio orvanel, meaning that the sun is at its center. 2. : having (something) as a central interest, influence, subject, in the case of this wine label it is Syrah wine from Walla Walla Valley
this american vitculture area is known for wines which showcase the terrior of the area - this wine is specifically from the Rocks district where there are lots of rocks in the vineyard. think terrior, rocks, dirt, grapes that are hand crafted into a bottle of wine that will cost $125 each.

Target Market(s)

syrah lovers, Rhone valley wine lovers,

Industry/Entity Type

wine industry

Font styles to use
Sans Serif
Other font styles liked:
• freightbig in light, book and medium weights

Requirements
Must have
• the elements described in the project description, please use FreightBig font found on quillo site, light, book and medium weights
Nice to have
• a cool edgy design but elegant a the same time
Should not have
• stock pictures

```html
<!DOCTYPE html>
<html lang="en">
<head>
<meta charset="UTF-8">
<title>Orvanel Syrah – Wine Label</title>
<link rel="stylesheet" href="https://fonts.googleapis.com/css2?family=Josefin+Sans:wght@300;400;600&family=Pinyon+Script&display=swap">
<style>
  :root {
    --canvas-bg: #ffffff;
    --label-bg: #f4f5f5;
    --ornament-core: #dcdede;
    --ornament-edge: rgba(220, 222, 222, 0);
    --wine-plum: #3a1427;
    --ink-black: #111111;
  }

  * { margin: 0; padding: 0; box-sizing: border-box; }

  html, body {
    width: 1200px;
    height: 1000px;
    overflow: hidden;
    background: var(--canvas-bg);
  }

  .canvas {
    position: relative;
    width: 1200px;
    height: 1000px;
    background: var(--canvas-bg);
  }

  .label {
    position: absolute;
    left: 220px;
    top: 160px;
    width: 760px;
    height: 680px;
    background: var(--label-bg);
  }

  .label__emblem {
    position: absolute;
    left: 152px;
    top: 35px;
    width: 446px;
    height: 446px;
    border-radius: 50%;
    background: radial-gradient(circle, var(--ornament-core) 0%, var(--ornament-core) 35%, var(--ornament-edge) 72%);
  }

  .label__brand {
    position: absolute;
    left: 0;
    width: 100%;
    top: 225px;
    text-align: center;
    font-family: "Josefin Sans", sans-serif;
    font-weight: 600;
    font-size: 60px;
    line-height: 1;
    letter-spacing: 0.42em;
    text-indent: 0.42em;
    color: var(--wine-plum);
  }

  .label__varietal {
    position: absolute;
    left: 0;
    width: 100%;
    top: 455px;
    text-align: center;
    font-family: "Pinyon Script", cursive;
    font-weight: 400;
    font-size: 104px;
    line-height: 1.2;
    color: var(--ink-black);
  }

  .label__region {
    position: absolute;
    left: 0;
    width: 100%;
    top: 608px;
    text-align: center;
    font-family: "Josefin Sans", sans-serif;
    font-weight: 300;
    font-size: 25px;
    line-height: 1;
    letter-spacing: 0.3em;
    text-indent: 0.3em;
    color: var(--wine-plum);
  }
</style>
</head>
<body>
  <main class="canvas">
    <section class="label" aria-label="Orvanel Syrah wine label">
      <div class="label__emblem" role="img" aria-label="Light grey radiating sunburst emblem of leaves, arrows and dotted rings"></div>
      <h1 class="label__brand">ORVANEL</h1>
      <p class="label__varietal">Syrah</p>
      <p class="label__region">WALLA WALLA VALLEY</p>
    </section>
  </main>
</body>
</html>
```